Eye catching business card

2 sided
Black background with logo in color on one side along with the words "Proudly serving the commercial and defense industries since 1975"
2nd side to contain contact information (see attached current business card) and "Waterjet, Composite, Precision Machining and Clean Room Manufacturing" with a very faint watermark of a waving USA Flag in the back ground.
Remove the "est. 195" from the current logo design

```html
<!DOCTYPE html>
<html lang="en">
<head>
<meta charset="utf-8">
<title>Vantor Machine Inc – Business Card</title>
<link href="https://fonts.googleapis.com/css2?family=Montserrat:wght@400;500;600;700&display=swap" rel="stylesheet">
<style>
  :root {
    --page: #1b1c1f;
    --card: #26282c;
    --card-deep: #1e2023;
    --mark: #141517;
    --text-light: #c9cbd0;
    --text-muted: #9a9ca2;
    --accent: #2f8fe6;
    --accent-deep: #2a5fc9;
    --rule: #8d9096;
  }
  * { box-sizing: border-box; margin: 0; padding: 0; }
  html, body { width: 1200px; height: 800px; overflow: hidden; }
  body {
    background: var(--page);
    font-family: "Montserrat", sans-serif;
    color: var(--text-light);
    position: relative;
  }
  .card {
    position: absolute;
    top: 100px;
    width: 340px;
    height: 595px;
    background: var(--card);
    border-radius: 22px;
    overflow: hidden;
  }
  .card--front { left: 190px; }
  .card--back { left: 670px; }

  /* Front */
  .front-mark {
    position: absolute;
    top: 0; left: 70px;
    width: 270px; height: 250px;
    background: var(--mark);
  }
  .front-statement {
    position: absolute;
    left: 0; right: 0; top: 300px;
    text-align: center;
    text-transform: uppercase;
    font-size: 17px;
    line-height: 1.45;
    letter-spacing: 1px;
    color: var(--text-muted);
  }
  .front-statement strong { font-weight: 700; color: var(--text-light); }
  .brand-name {
    font-weight: 600;
    text-transform: uppercase;
    letter-spacing: 2px;
    color: var(--text-light);
  }
  .front-brand {
    position: absolute;
    left: 0; right: 0; top: 450px;
    text-align: center;
    font-size: 22px;
    padding-bottom: 10px;
  }
  .front-brand::after {
    content: "";
    display: block;
    width: 230px; height: 1px;
    margin: 10px auto 0;
    background: var(--rule);
  }
  .edge-band {
    position: absolute;
    left: 0; right: 0; bottom: 0;
    height: 14px;
    background: linear-gradient(90deg, var(--accent), var(--accent-deep));
  }

  /* Back */
  .flag-watermark {
    position: absolute;
    left: 0; top: 210px;
    width: 260px; height: 310px;
    background: linear-gradient(160deg, #2c2e33 0%, var(--card-deep) 70%, transparent 100%);
    opacity: .7;
  }
  .back-brand {
    position: absolute;
    top: 40px; right: 28px;
    display: flex; align-items: center; gap: 12px;
  }
  .back-brand .brand-square {
    width: 34px; height: 34px;
    background: var(--accent);
  }
  .back-brand .brand-name { font-size: 20px; }
  .contact {
    position: absolute;
    left: 30px; right: 28px; top: 125px;
    text-align: right;
    font-size: 14px;
    line-height: 1.55;
  }
  .contact-name { font-size: 19px; font-weight: 700; letter-spacing: 1px; text-transform: uppercase; }
  .contact-role { color: var(--accent); font-size: 14px; margin-bottom: 10px; }
  .company { font-size: 18px; font-weight: 700; margin-top: 34px; }
  .services { margin-bottom: 16px; }
  .line { display: flex; justify-content: flex-end; align-items: center; gap: 7px; }
  .line svg { width: 13px; height: 13px; fill: var(--accent); }
  .web-band {
    position: absolute;
    left: 0; right: 0; bottom: 0;
    height: 58px;
    background: linear-gradient(90deg, var(--accent-deep), var(--accent));
    border-top: 3px solid #c9cbd0;
    display: flex; align-items: center; justify-content: center;
    color: #0f1a2b;
    font-size: 16px;
    letter-spacing: 1px;
  }
  .web-band b { font-weight: 700; }
</style>
</head>
<body>
  <section class="card card--front" aria-label="Card front">
    <div class="front-mark" aria-hidden="true"></div>
    <p class="front-statement">
      Proudly serving<br>
      <strong>the commercial and</strong><br>
      defense industries<br>
      <strong>since 1975</strong>
    </p>
    <p class="brand-name front-brand">Vantor Machine Inc</p>
    <div class="edge-band"></div>
  </section>

  <section class="card card--back" aria-label="Card back">
    <div class="flag-watermark" role="img" aria-label="Faint waving USA flag watermark"></div>
    <div class="back-brand">
      <span class="brand-square" aria-hidden="true"></span>
      <span class="brand-name">Vantor Machine Inc</span>
    </div>
    <div class="contact">
      <p class="contact-name">Dale Warren</p>
      <p class="contact-role">President</p>
      <p>Office: 410-555-0148</p>
      <p>dale@vantormachine.com</p>
      <p class="company">Vantor Machine, Inc.</p>
      <p class="services">Waterjets, Composites &amp; Precision Machining</p>
      <p>214 West Harlan Rd.</p>
      <p>Glen Ridge, PA 17302</p>
      <p class="line">
        <svg viewBox="0 0 24 24" aria-hidden="true"><path d="M6.6 10.8a15 15 0 0 0 6.6 6.6l2.2-2.2a1 1 0 0 1 1-.25 11.4 11.4 0 0 0 3.6.57 1 1 0 0 1 1 1V20a1 1 0 0 1-1 1A17 17 0 0 1 3 4a1 1 0 0 1 1-1h3.5a1 1 0 0 1 1 1c0 1.25.2 2.45.57 3.6a1 1 0 0 1-.25 1z"/></svg>
        410-555-0148
      </p>
      <p class="line">
        <svg viewBox="0 0 24 24" aria-hidden="true"><path d="M6 3h9v5H6zM4 9h16a2 2 0 0 1 2 2v6h-4v4H6v-4H2v-6a2 2 0 0 1 2-2zm4 7v3h8v-3z"/></svg>
        410-555-0172
      </p>
      <p>info@vantormachine.com</p>
    </div>
    <div class="web-band">www.<b>VANTORMACHINE</b>.com</div>
  </section>
</body>
</html>
```